Letterhead and Envelope for Mental Health Business

I need letterhead and envelope designs that will match my business cards. I am attaching a *.pds file of my business card so it can be matched.

```html
<!DOCTYPE html>
<html lang="en">
<head>
<meta charset="utf-8">
<title>Linden Counseling Stationery</title>
<link rel="stylesheet" href="https://fonts.googleapis.com/css2?family=Arimo:wght@400;700&display=swap">
<style>
  :root {
    --bg: #efe8dc;
    --paper: #ffffff;
    --blue-dark: #2a4e94;
    --blue-mid: #2f6fb8;
    --blue-light: #3fa2dc;
    --green: #4f8a2e;
    --text-blue: #2a4a8c;
    --faint: #e6ecf4;
  }
  * { box-sizing: border-box; margin: 0; padding: 0; }
  html, body { width: 1032px; height: 1200px; overflow: hidden; }
  body {
    position: relative;
    background: var(--bg);
    font-family: "Arimo", Arial, sans-serif;
    color: var(--text-blue);
  }
  .sheet { position: absolute; background: var(--paper); box-shadow: 0 4px 14px rgba(0,0,0,.22); overflow: hidden; }

  /* Letterhead */
  .letterhead { left: 262px; top: 110px; width: 730px; height: 945px; }
  .letterhead__header { position: absolute; left: 0; top: 0; width: 730px; height: 140px; }
  .letterhead__mark { position: absolute; right: -120px; top: 260px; width: 480px; height: 480px; }
  .letterhead .brand { position: absolute; left: 40px; top: 150px; }
  .letterhead__footer {
    position: absolute; left: 30px; right: 30px; bottom: 24px;
    display: flex; justify-content: space-between;
    border-top: 2px solid var(--green); padding-top: 10px;
    font-size: 11px; white-space: nowrap;
  }

  /* Brand name */
  .brand { display: flex; align-items: center; gap: 8px; }
  .brand__dot { width: 30px; height: 30px; border-radius: 50%; background: var(--green); flex: none; }
  .brand__name { font-weight: 700; color: var(--blue-dark); font-size: 26px; letter-spacing: .5px; }

  .label { color: var(--green); font-weight: 700; }

  /* Business card */
  .card { left: 40px; top: 400px; width: 380px; height: 214px; z-index: 2; }
  .card .brand { position: absolute; left: 64px; top: 16px; }
  .card .brand__dot { width: 22px; height: 22px; }
  .card .brand__name { font-size: 19px; }
  .card__person { position: absolute; left: 0; right: 0; top: 58px; text-align: center; }
  .card__name { font-size: 17px; font-weight: 700; letter-spacing: 2px; color: var(--blue-dark); }
  .card__creds { font-size: 8px; font-weight: 700; letter-spacing: 1px; color: var(--green); margin-top: 3px; }
  .card__band {
    position: absolute; left: 0; right: 0; bottom: 0; height: 98px;
    background: linear-gradient(90deg, var(--blue-mid), var(--blue-dark));
    padding: 14px 0 0 22px; color: #fff; font-size: 10.5px; line-height: 17px; letter-spacing: .6px;
  }
  .card__band small { display: inline-block; width: 34px; font-size: 6px; opacity: .7; }

  /* Envelope */
  .envelope { left: 60px; top: 640px; width: 740px; height: 320px; z-index: 1; }
  .envelope .brand { position: absolute; left: 30px; top: 24px; }
  .envelope__address { position: absolute; left: 44px; top: 74px; font-size: 11.5px; line-height: 15px; }
  .envelope__band { position: absolute; left: 0; bottom: 0; width: 740px; height: 64px; }
</style>
</head>
<body>

<section class="sheet letterhead" aria-label="Letterhead">
  <svg class="letterhead__header" viewBox="0 0 730 140" aria-hidden="true">
    <defs>
      <linearGradient id="headBlue" x1="0" x2="1">
        <stop offset="0" stop-color="#3fa2dc"/>
        <stop offset="1" stop-color="#2a4e94"/>
      </linearGradient>
    </defs>
    <path d="M0 0 H730 V125 C560 45 260 30 0 42 Z" fill="url(#headBlue)"/>
  </svg>
  <svg class="letterhead__mark" viewBox="0 0 100 100" aria-hidden="true">
    <circle cx="50" cy="50" r="46" fill="none" stroke="#e6ecf4" stroke-width="6"/>
  </svg>
  <div class="brand"><span class="brand__dot"></span><span class="brand__name">Linden Counseling</span></div>
  <p class="letterhead__footer">
    <span><b class="label">A:</b> Harbor Lane 48, 2150 Portland, USA</span>
    <span><b class="label">P:</b> 555/014-2290</span>
    <span><b class="label">E:</b> mara@lindencounseling.com</span>
    <span><b class="label">W:</b> www.lindencounseling.com</span>
  </p>
</section>

<section class="sheet card" aria-label="Business card">
  <div class="brand"><span class="brand__dot"></span><span class="brand__name">Linden Counseling</span></div>
  <div class="card__person">
    <p class="card__name">Mara Ellison</p>
    <p class="card__creds">LMHC, NCC, DCC</p>
  </div>
  <div class="card__band">
    <p><small>addr</small>Harbor Lane 48, 2150 Portland, USA</p>
    <p><small>phone</small>555/014-2290</p>
    <p><small>mail</small>mara@lindencounseling.com</p>
    <p><small>web</small>www.lindencounseling.com</p>
  </div>
</section>

<section class="sheet envelope" aria-label="Envelope">
  <div class="brand"><span class="brand__dot"></span><span class="brand__name">Linden Counseling</span></div>
  <div class="envelope__address">
    <p><b class="label">A:</b> Harbor Lane 48, 2150 Portland, USA</p>
    <p><b class="label">P:</b> 555/014-2290</p>
    <p><b class="label">E:</b> mara@lindencounseling.com</p>
    <p><b class="label">W:</b> www.lindencounseling.com</p>
  </div>
  <svg class="envelope__band" viewBox="0 0 740 64" preserveAspectRatio="none" aria-hidden="true">
    <defs>
      <linearGradient id="envBlue" x1="0" y1="0" x2="0" y2="1">
        <stop offset="0" stop-color="#2f6fb8"/>
        <stop offset="1" stop-color="#2a4e94"/>
      </linearGradient>
    </defs>
    <rect x="0" y="8" width="740" height="6" fill="#3fa2dc"/>
    <rect x="0" y="14" width="740" height="50" fill="url(#envBlue)"/>
  </svg>
</section>

</body>
</html>
```